Corvath Alloyworks Inc. I'm looking for flyer bi-fold the gives the customer a snapshot of o...

Take this text and consolidate and paint the story with images. All this text is for information for the designer. I have up loaded some old flyers also. Through our distribution partners, we supply pipe, tube, fittings and valves to such industries as food and dairy, biopharmaceutical, ethanol, meat packing, pulp and paper and semiconductor.Originally focused on the custom manufacture of stainless pipe/tube fittings, CAI has evolved into a stocking manufacturer of 45° laterals, reducing tees, custom reducers, polished pipe and tube, and many other unique or difficult to find piping products. We have coupled that with an inventory of more mainstream fittings to provide one-stop procurement for many of our distributors stainless needs.We offer our customers many specialty fittings, flanges, fabrication and custom machining with a heavy focus on fast turnaround. Our normal turnaround on most custom fittings is 5-7 working days; If you require it sooner - ask!! We work with customers to find the solution that best fits the circumstance, be it air freight, expedited delivery, special packaging or other needs.At CAI, you will find a company that is small enough to be nimble — adjusting shop schedules to adhere to the most demanding of customers’ lead-time requirements. Yet we are large enough to handle small to medium sized projects with confidence. Our shop is structured for the expedience and efficiency you must have. With our focus on fast turnaround, you and your customer enjoy the peace of mind that we will have your fittings done on time and shipped when you want.
Font styles to use
Look and feel
Each slider illustrates characteristics of the customer's brand and the style your logo design should communicate.

```html
<!DOCTYPE html>
<html lang="en">
<head>
<meta charset="utf-8">
<title>Corvath Alloyworks Inc. — Bi-fold Flyer Interior</title>
<link rel="stylesheet" href="https://fonts.googleapis.com/css2?family=Montserrat:wght@400;500;600;700&family=Oswald:wght@400;500;600&display=swap">
<style>
  :root {
    --red: #b5121b;
    --red-deep: #8f0d14;
    --ink: #231f20;
    --text: #4a4a4a;
    --paper: #f7f7f5;
    --backdrop: #d9d9dc;
    --thumb: #2a2a2c;
  }
  * { box-sizing: border-box; margin: 0; padding: 0; }
  html, body { width: 1200px; height: 840px; overflow: hidden; }
  body {
    background: var(--backdrop);
    font-family: "Montserrat", Arial, sans-serif;
    color: var(--text);
    position: relative;
  }
  .page {
    position: absolute;
    top: 38px;
    width: 540px;
    height: 764px;
    background: var(--paper);
    overflow: hidden;
  }
  .page--left { left: 60px; box-shadow: inset -14px 0 20px -16px rgba(0,0,0,.25); }
  .page--right { left: 600px; box-shadow: inset 14px 0 20px -16px rgba(0,0,0,.25); }

  /* Left page */
  .team-photo {
    position: absolute; left: 250px; top: 0; width: 290px; height: 350px;
    background: linear-gradient(160deg, #c9c6c1 0%, #a98a66 35%, #e6e3de 55%, #6b6b70 80%, #d2cfca 100%);
    clip-path: polygon(18% 0, 100% 0, 100% 100%, 45% 100%, 0 60%);
  }
  .tagline-banner {
    position: absolute; left: 150px; top: 168px; width: 330px; height: 46px;
    background: var(--red);
    color: #fff;
    font-family: "Oswald", Arial, sans-serif;
    font-size: 21px; font-weight: 400;
    display: flex; align-items: center; justify-content: center;
    transform: rotate(-7deg);
    box-shadow: 0 4px 10px rgba(0,0,0,.25);
  }
  .section-title {
    font-family: "Oswald", Arial, sans-serif;
    font-size: 13px; font-weight: 500;
    letter-spacing: 3px;
    color: var(--ink);
    text-transform: uppercase;
  }
  .about { position: absolute; left: 34px; top: 262px; width: 224px; }
  .about .section-title { text-align: center; margin-bottom: 12px; }
  .about p { font-size: 10px; line-height: 1.6; text-align: justify; }
  .services { position: absolute; left: 300px; top: 390px; width: 220px; }
  .services .section-title { text-align: center; margin-bottom: 16px; }
  .service { display: flex; align-items: center; gap: 14px; margin-bottom: 22px; }
  .service-thumb {
    width: 66px; height: 66px; flex: none;
    border: 4px solid var(--red); border-radius: 12px;
    background: radial-gradient(circle at 40% 40%, #9a9a9c 0%, #4a4a4d 45%, #1c1c1e 100%);
  }
  .service-label {
    font-size: 8.5px; font-weight: 700; line-height: 1.45;
    text-transform: uppercase; color: var(--ink);
  }

  /* Right page */
  .headline { position: absolute; left: 40px; top: 66px; }
  .headline h2 {
    font-family: "Oswald", Arial, sans-serif;
    font-size: 25px; font-weight: 400; line-height: 1.15;
    letter-spacing: 5px; color: var(--ink); text-transform: uppercase;
  }
  .headline .sizes { margin-top: 8px; font-size: 10.5px; font-weight: 700; color: var(--ink); letter-spacing: .5px; }
  .products { position: absolute; left: 40px; top: 180px; width: 300px; }
  .product { display: flex; align-items: center; gap: 22px; height: 96px; }
  .product-thumb {
    width: 92px; height: 64px; flex: none;
    background: linear-gradient(135deg, #3a3a3c, var(--thumb));
    border: 1px solid #111;
    box-shadow: 0 2px 4px rgba(0,0,0,.3);
  }
  .product-name {
    font-family: "Oswald", Arial, sans-serif;
    font-size: 10px; font-weight: 500; letter-spacing: 2.5px;
    color: var(--red); text-transform: uppercase; margin-bottom: 3px;
  }
  .product-types { font-size: 9.5px; line-height: 1.4; color: var(--text); }
  .weld-photo {
    position: absolute; right: 0; top: 0; width: 150px; height: 500px;
    background: radial-gradient(circle at 45% 45%, #ffd48a 0%, #e07a2a 10%, #5a7ea8 24%, #1f2c3f 48%, #0c0f16 100%);
  }
  .cta-panel { position: absolute; right: 0; bottom: 0; width: 215px; height: 330px; }
  .cta-panel svg { position: absolute; inset: 0; }
  .cta-content { position: absolute; left: 22px; right: 18px; top: 98px; color: #fff; }
  .cta-content h3 {
    font-family: "Oswald", Arial, sans-serif;
    font-size: 19px; font-weight: 500; line-height: 1.2;
    text-align: right; text-transform: uppercase; letter-spacing: .5px;
  }
  .cta-content .also { margin-top: 14px; font-size: 8px; font-weight: 700; letter-spacing: 1px; }
  .build-list { display: flex; gap: 10px; margin-top: 6px; }
  .build-list ul { list-style: none; font-size: 7.5px; line-height: 1.5; flex: 1; }
  .build-list li::before { content: "- "; }
</style>
</head>
<body>
  <section class="page page--left">
    <div class="team-photo" role="img" aria-label="Photo of a team working together at a table with laptops"></div>
    <div class="tagline-banner">Making it happen on YOUR schedule</div>

    <div class="about">
      <h2 class="section-title">About Us</h2>
      <p>Corvath Alloyworks Inc. (CAI) supplies pipe, tube, fittings and valves through our distribution partners to industries such as food and dairy, biopharmaceutical, ethanol, meat packing, pulp and paper and semiconductor. Originally focused on the custom manufacture of stainless pipe and tube fittings, CAI has evolved into a stocking manufacturer of 45° laterals, reducing tees, custom reducers, polished pipe and tube, and many other unique or hard to find piping products. We have coupled that with an inventory of mainstream fittings to provide one-stop procurement for many of our distributors' stainless needs.</p>
    </div>

    <div class="services">
      <h2 class="section-title">Our Services</h2>
      <div class="service">
        <div class="service-thumb" role="img" aria-label="Photo of a stainless steel manifold"></div>
        <p class="service-label">Custom stainless steel<br>manifolds &amp; specialty<br>assemblies</p>
      </div>
      <div class="service">
        <div class="service-thumb" role="img" aria-label="Photo of a polished stainless elbow fitting"></div>
        <p class="service-label">Custom stainless<br>fittings &amp; flanges</p>
      </div>
      <div class="service">
        <div class="service-thumb" role="img" aria-label="Photo of stainless pipe ends"></div>
        <p class="service-label">Custom stainless<br>pipe &amp; tube cuts</p>
      </div>
    </div>
  </section>

  <section class="page page--right">
    <div class="headline">
      <h2>Extreme Reduction<br>Unusual Size</h2>
      <p class="sizes">OD X IPS &nbsp;|&nbsp; IPS X METRIC &nbsp;|&nbsp; OD X METRIC</p>
    </div>

    <div class="products">
      <div class="product">
        <div class="product-thumb" role="img" aria-label="Technical drawing of a reducer"></div>
        <div><p class="product-name">Reducers</p><p class="product-types">Concentric<br>Eccentric Tangent Reducer<br>Cone Reducer</p></div>
      </div>
      <div class="product">
        <div class="product-thumb" role="img" aria-label="Technical drawing of a multi-port manifold"></div>
        <div><p class="product-name">Multi-Port Manifold</p><p class="product-types">Variety of angles</p></div>
      </div>
      <div class="product">
        <div class="product-thumb" role="img" aria-label="Technical drawing of a cross fitting"></div>
        <div><p class="product-name">Crosses</p><p class="product-types">Standard<br>Reducing</p></div>
      </div>
      <div class="product">
        <div class="product-thumb" role="img" aria-label="Technical drawing of a true wye"></div>
        <div><p class="product-name">True Wyes</p><p class="product-types">Reducing True Wye<br>Reducing (run) True</p></div>
      </div>
      <div class="product">
        <div class="product-thumb" role="img" aria-label="Technical drawing of a lateral fitting"></div>
        <div><p class="product-name">Laterals</p><p class="product-types">45 degree Lateral<br>30 degree Lateral<br>45 degree Lateral Tee</p></div>
      </div>
    </div>

    <div class="weld-photo" role="img" aria-label="Photo of welding with flying sparks"></div>

    <div class="cta-panel">
      <svg width="215" height="330" viewBox="0 0 215 330" aria-hidden="true">
        <polygon points="0,90 215,0 215,330 0,330" fill="var(--red)"/>
        <polygon points="0,90 215,0 215,14 0,104" fill="var(--red-deep)" opacity=".5"/>
      </svg>
      <div class="cta-content">
        <h3>Still don't<br>see what you're<br>looking for?</h3>
        <p class="also">WE ALSO BUILD:</p>
        <div class="build-list">
          <ul>
            <li>Mitered Swages</li>
            <li>Reducing Elbows</li>
            <li>180° Elbows</li>
            <li>Pipe Flanges</li>
            <li>Pad Flanges</li>
            <li>Sanitary Flanges</li>
            <li>Reinforcing Pads for Tee Branches</li>
          </ul>
          <ul>
            <li>Paddle Blinds</li>
            <li>Spectacle Blinds</li>
            <li>Blind Rings</li>
            <li>Bolt Rings</li>
            <li>Stub Ends</li>
            <li>Flanged Fittings</li>
            <li>Pipe Cuts</li>
          </ul>
        </div>
      </div>
    </div>
  </section>
</body>
</html>
```